Business Card Design Project

We would like to have a new design for our Business Cards.
Please see attached JPEG to see the current.
We would like to be sober and clean, very professional.

Target Market(s)

IT Market

Industry/Entity Type

Business

Font styles to use
Serif
Sans Serif

Colors
ec1f27
f78f20
333333
5c5c5c
9d9d9d
e9e9e9
ffffff

Requirements
Must have
• It needs to be completely different than the current design (see attached),

```html
<!DOCTYPE html>
<html lang="en">
<head>
<meta charset="utf-8">
<title>NovaLink Business Card</title>
<link rel="stylesheet" href="https://fonts.googleapis.com/css2?family=Cinzel:wght@400;600&family=Jost:wght@400;500;700;800&display=swap">
<style>
  :root {
    --red: #ec1f27;
    --red-deep: #b8151b;
    --orange: #f78f20;
    --ink: #333333;
    --grey-dark: #5c5c5c;
    --grey-mid: #9d9d9d;
    --grey-light: #e9e9e9;
    --white: #ffffff;
    --black: #141414;
    --stage: #d9d9d9;
  }
  * { box-sizing: border-box; margin: 0; padding: 0; }
  html, body {
    width: 1200px; height: 1023px; overflow: hidden;
    background: var(--stage);
    font-family: "Jost", Arial, sans-serif;
  }
  .stage {
    width: 1200px; height: 1023px;
    display: flex; flex-direction: column;
    align-items: center; justify-content: center; gap: 60px;
  }
  .card {
    width: 660px; height: 377px;
    position: relative; overflow: hidden;
    box-shadow: 0 10px 28px rgba(0,0,0,.22);
  }

  /* Front: logo + address */
  .card-front {
    background: linear-gradient(160deg, var(--white) 0%, #f3f3f3 100%);
  }
  .brand {
    position: absolute; left: 150px; top: 120px;
    display: flex; align-items: center; gap: 18px;
  }
  .brand-dot {
    width: 62px; height: 62px; border-radius: 50%;
    background: var(--red);
  }
  .brand-name {
    font-weight: 800; font-size: 62px; color: var(--ink);
    letter-spacing: -1px; line-height: 1;
  }
  .address {
    position: absolute; right: 44px; bottom: 44px;
    width: 320px;
    font-size: 17px; line-height: 1.35; color: var(--ink);
    padding-top: 14px;
    border-top: 2px solid var(--red);
  }

  /* Back: name plate + contact bars */
  .card-back {
    background: linear-gradient(170deg, #2b2b2b 0%, var(--black) 55%, #000 100%);
  }
  .name-plate {
    position: absolute; left: 34px; top: 78px;
    width: 250px; height: 150px;
    background: var(--white); border-radius: 8px;
    padding: 34px 22px 0 22px;
  }
  .name-plate::before {
    content: ""; position: absolute; top: 12px; left: 22px; right: 22px;
    height: 1px; background: var(--red);
  }
  .person-name {
    font-family: "Cinzel", Georgia, serif; font-weight: 400;
    font-size: 27px; color: var(--ink); letter-spacing: 1px;
    padding-bottom: 8px; border-bottom: 1px solid var(--grey-mid);
    white-space: nowrap;
  }
  .person-role {
    margin-top: 8px; font-size: 17px; color: var(--red-deep);
  }
  .contacts {
    position: absolute; left: 310px; right: 0; top: 150px;
    display: flex; flex-direction: column; gap: 18px;
  }
  .contact {
    display: flex; align-items: center; gap: 12px;
    height: 40px; padding-left: 12px;
    background: linear-gradient(90deg, var(--red) 0%, var(--red-deep) 100%);
    color: var(--white); font-size: 18px;
    border-radius: 4px 0 0 4px;
  }
  .contact svg { width: 22px; height: 22px; flex: none; }
  .back-rule {
    position: absolute; left: 0; right: 0; bottom: 0; height: 10px;
    background: var(--red);
  }
</style>
</head>
<body>
<main class="stage">
  <section class="card card-front" aria-label="Card front">
    <div class="brand">
      <span class="brand-dot"></span>
      <span class="brand-name">NovaLink</span>
    </div>
    <p class="address">4120 N Cedar Ridge Blvd Suite 150<br>Riverton, AZ 85000</p>
  </section>

  <section class="card card-back" aria-label="Card back">
    <div class="name-plate">
      <p class="person-name">DANIEL HART</p>
      <p class="person-role">President &amp; CEO</p>
    </div>
    <div class="contacts">
      <p class="contact">
        <svg viewBox="0 0 24 24" fill="#fff" aria-hidden="true"><path d="M6.6 10.8a15.2 15.2 0 0 0 6.6 6.6l2.2-2.2a1 1 0 0 1 1-.25 11.4 11.4 0 0 0 3.6.57 1 1 0 0 1 1 1V20a1 1 0 0 1-1 1A17 17 0 0 1 3 4a1 1 0 0 1 1-1h3.5a1 1 0 0 1 1 1c0 1.25.2 2.45.57 3.57a1 1 0 0 1-.25 1z"/></svg>
        (555) 014-2290 Ext. 310
      </p>
      <p class="contact">
        <svg viewBox="0 0 24 24" fill="#fff" aria-hidden="true"><path d="M3 5h18v14H3z" fill="none" stroke="#fff" stroke-width="2"/><path d="M3 5l9 8 9-8" fill="none" stroke="#fff" stroke-width="2"/></svg>
        Daniel.Hart@NovaLink.com
      </p>
      <p class="contact">
        <svg viewBox="0 0 24 24" fill="none" stroke="#fff" stroke-width="1.8" aria-hidden="true"><circle cx="12" cy="12" r="9"/><ellipse cx="12" cy="12" rx="4" ry="9"/><path d="M3 12h18M5 7h14M5 17h14"/></svg>
        www.NovaLink.com
      </p>
    </div>
    <div class="back-rule"></div>
  </section>
</main>
</body>
</html>
```